New business card for civil engineering company - "Keystone Audit"

We need a business card designed for our new structural engineering company.

The company name is "Keystone Audit" logo files attached.

We would like the following:
* Two-sided card
* Simple design

Information to be placed on the card:
Name - Marcus Dellow
Job Title - Director / Structural Engineer
Credentials - BEng(Hons), CPEng, CMengNZ, IntPE(NZ)
Email - marcus.dellow@keystoneaudit.co.nz
mobile - 0219364058
website - www.keystoneaudit.co.nz

```html
<!DOCTYPE html>
<html lang="en">
<head>
<meta charset="utf-8">
<title>Keystone Audit – Business Card</title>
<link rel="stylesheet" href="https://fonts.googleapis.com/css2?family=Montserrat:wght@400;500;600;700&family=Quicksand:wght@400;500;600;700&display=swap">
<style>
  :root {
    --backdrop: #dcdcdc;
    --card-light: #f4f4f4;
    --brand-blue: #318dc9;
    --name-navy: #0f3f6a;
    --ink-dark: #333333;
    --ink-soft: #555555;
    --white: #ffffff;
  }
  * { box-sizing: border-box; margin: 0; padding: 0; }
  html, body { width: 1200px; height: 1200px; overflow: hidden; }
  body { background: var(--backdrop); position: relative; font-family: "Quicksand", sans-serif; }

  .card {
    position: absolute;
    left: 163px;
    width: 874px;
    height: 495px;
    border-radius: 12px;
    overflow: hidden;
  }
  .card--front { top: 79px; background: var(--card-light); }
  .card--back { top: 625px; background: var(--brand-blue); }

  .front-band { position: absolute; inset: 0; width: 100%; height: 100%; }

  .brand {
    position: absolute;
    display: flex;
    align-items: center;
    gap: 14px;
    font-family: "Montserrat", sans-serif;
    font-weight: 600;
    font-size: 30px;
    letter-spacing: 0.04em;
    white-space: nowrap;
  }
  .brand__mark { width: 22px; height: 22px; flex: none; }
  .brand--front { left: 227px; top: 151px; transform: translate(-50%, -50%); color: var(--ink-dark); }
  .brand--front .brand__mark { background: var(--brand-blue); }
  .brand--back { left: 50%; top: 187px; transform: translate(-50%, -50%); color: var(--white); font-size: 34px; }
  .brand--back .brand__mark { background: var(--white); width: 24px; height: 24px; }

  .person {
    position: absolute;
    left: 593px;
    top: 98px;
    transform: translateX(-50%);
    text-align: center;
    white-space: nowrap;
  }
  .person__name {
    font-family: "Montserrat", sans-serif;
    font-size: 40px;
    letter-spacing: 0.02em;
    color: var(--name-navy);
    line-height: 1;
    text-transform: uppercase;
  }
  .person__first { font-weight: 700; }
  .person__last { font-weight: 400; }
  .person__title {
    margin-top: 10px;
    font-size: 18px;
    font-weight: 500;
    color: var(--ink-dark);
  }
  .person__credentials {
    margin-top: 40px;
    font-size: 15px;
    font-weight: 500;
    color: var(--ink-soft);
    word-spacing: 2px;
  }

  .contact {
    position: absolute;
    top: 432px;
    transform: translateY(-50%);
    display: flex;
    align-items: center;
    gap: 10px;
    color: var(--white);
    white-space: nowrap;
  }
  .contact svg { flex: none; }
  .contact--email { left: 122px; font-size: 22px; font-weight: 500; }
  .contact--phone { left: 566px; font-size: 29px; font-weight: 700; letter-spacing: 0.01em; }

  .website {
    position: absolute;
    left: 0;
    right: 0;
    top: 436px;
    transform: translateY(-50%);
    text-align: center;
    color: var(--white);
    font-family: "Montserrat", sans-serif;
    font-weight: 600;
    font-size: 19px;
    letter-spacing: 0.42em;
  }
</style>
</head>
<body>
  <section class="card card--front" aria-label="Business card front">
    <svg class="front-band" viewBox="0 0 874 495" preserveAspectRatio="none" aria-hidden="true">
      <polygon points="0,389 874,341 874,495 0,495" fill="var(--brand-blue)"/>
    </svg>

    <div class="brand brand--front">
      <span class="brand__mark"></span>
      <span class="brand__name">Keystone Audit</span>
    </div>

    <div class="person">
      <h1 class="person__name"><span class="person__first">Marcus</span> <span class="person__last">Dellow</span></h1>
      <p class="person__title">Director / Structural Engineer</p>
      <p class="person__credentials">BEng(Hons) | CPEng | CMengNZ | IntPE(NZ)</p>
    </div>

    <div class="contact contact--email">
      <svg width="26" height="22" viewBox="0 0 26 22" aria-hidden="true">
        <path d="M2 8 L13 1 L24 8 V21 H2 Z" fill="none" stroke="var(--white)" stroke-width="2" stroke-linejoin="round"/>
        <path d="M2 8 L13 15 L24 8" fill="none" stroke="var(--white)" stroke-width="2" stroke-linejoin="round"/>
      </svg>
      <span>marcus.dellow@keystoneaudit.co.nz</span>
    </div>

    <div class="contact contact--phone">
      <svg width="26" height="26" viewBox="0 0 24 24" aria-hidden="true">
        <path d="M6.6 10.8a15 15 0 0 0 6.6 6.6l2.2-2.2a1 1 0 0 1 1-.25 11.4 11.4 0 0 0 3.6.57 1 1 0 0 1 1 1V20a1 1 0 0 1-1 1A17 17 0 0 1 3 4a1 1 0 0 1 1-1h3.5a1 1 0 0 1 1 1c0 1.25.2 2.45.57 3.6a1 1 0 0 1-.25 1z" fill="var(--white)"/>
      </svg>
      <span>0219364058</span>
    </div>
  </section>

  <section class="card card--back" aria-label="Business card back">
    <div class="brand brand--back">
      <span class="brand__mark"></span>
      <span class="brand__name">Keystone Audit</span>
    </div>
    <p class="website">www.keystoneaudit.co.nz</p>
  </section>
</body>
</html>
```